New Consulting Firm News PowerPoint Template

We are a new consulting firm that specializes in Veltrix Unified Planning Suite implementations in need of a new PowerPoint template. We need at least the following layouts:
• Main Cover Slide
• Agenda / Table of Contents
• Title slide for each of the agenda items leading into actual content
• Title + Content with nice bullets in the content
• Title + Sub-Title + Content with nice bullets in the content
• Title + Two Columns of Content
• Title + Sub-Title + Two Columns of Content
• Title + Three Columns of Content
• Title + Sub-Title + Three Columns of Content
• Title + Two Rows and Two Columns of Content (4 boxes)
• Title + Sub-Title + Two Rows and Two Columns of Content (4 boxes)
• Title + Blank
• Nascar Slide (Client logos arranged somehow)
• Case Study Slide
• Various infographic slides than can be used and modified would be amazing as well
Our logo has been uploaded and you can find our website here:
https://brannowadvisory.com
We would like the main theme colors to blend with our logo, but also have a variety of colors in the theme that compliment the main theme colors. Once we have selected a PowerPoint design we expect to immediately have a Word design contest and the winning PowerPoint design will likely be a heavy influence on the Word design.

Target Market(s)

CFO, CAO, VP of Finance, Controllers

Industry/Entity Type

Consulting

Font styles to use
Serif
Sans Serif

Requirements
Must have
• • Main Cover Slide
• Title + Blank
• Case Study Slide
Nice to have
• • Various infographic slides than can be used and modified would be amazing as well

```html
<!DOCTYPE html>
<html lang="en">
<head>
<meta charset="utf-8">
<title>Brannow Advisory – Presentation Template</title>
<link href="https://fonts.googleapis.com/css2?family=IBM+Plex+Sans:wght@400;500;700&display=swap" rel="stylesheet">
<style>
  :root{
    --canvas:#c8c9cb;
    --blue:#1f5bb5;
    --charcoal:#58595b;
    --ink:#1d1d1f;
    --body:#2f2f33;
    --tint:#f3f0f3;
    --white:#ffffff;
    --rule:#d4d0d4;
  }
  *{box-sizing:border-box;margin:0;padding:0}
  html,body{width:1200px;height:4311px;overflow:hidden}
  body{background:var(--canvas);font-family:"IBM Plex Sans",Arial,sans-serif;color:var(--body);position:relative}
  .slide{position:absolute;left:80px;width:1048px;height:787px;overflow:hidden}
  .slide--cover{top:70px;background:var(--white)}
  .slide--columns{top:916px;background:var(--tint)}
  .slide--services{top:1749px;background:var(--tint)}
  .slide--twocol{top:2583px;background:var(--tint)}
  .slide--values{top:3435px}
  .abs{position:absolute}

  /* brand lockup */
  .brand{position:absolute;display:flex;flex-direction:column;align-items:center;gap:10px}
  .brand__mark{width:44px;height:44px;background:var(--blue)}
  .brand__name{font-size:22px;font-weight:500;letter-spacing:3px;color:var(--blue);line-height:1.2;text-align:center}
  .brand--center{left:0;right:0;top:46px}

  /* bullets */
  .bullets{list-style:none}
  .bullets li{position:relative;padding-left:20px}
  .bullets li::before{content:"";position:absolute;left:2px;top:50%;transform:translateY(-50%);border-left:6px solid currentColor;border-top:5px solid transparent;border-bottom:5px solid transparent}

  /* cover */
  .cover__art{position:absolute;left:0;top:0;width:1048px;height:787px}
  .cover__photo{left:0;top:204px;width:360px;height:429px;background:linear-gradient(135deg,#e9edf2 0%,#c9d3dd 45%,#8fb3b4 70%,#e3e7ec 100%)}
  .cover__rule{left:618px;top:122px;width:70px;height:2px;background:var(--white)}
  .cover__title{left:403px;width:500px;top:168px;text-align:center;color:var(--white);font-size:30px;font-weight:700;letter-spacing:.5px}
  .cover__lead{left:403px;width:500px;top:262px;text-align:center;color:var(--white);font-size:19px;line-height:24px}
  .cover__bullets{left:460px;top:476px;color:var(--white);font-size:19px;line-height:32.6px}

  /* section titles */
  .heading{position:absolute;left:0;right:0;text-align:center;color:var(--ink);font-weight:700}
  .subheading{position:absolute;left:0;right:0;text-align:center;color:var(--ink)}

  /* three column cards */
  .card{position:absolute;background:var(--white)}
  .card--text{top:281px;width:316px;height:452px;padding:50px 37px 0}
  .card__title{font-size:19px;font-weight:500;line-height:27px;color:var(--ink);text-transform:uppercase}
  .card__body{margin-top:15px;font-size:16.5px;line-height:21.7px;color:var(--body)}

  /* services */
  .card--service{top:306px;width:314px;height:439px;text-align:center}
  .service__photo{width:100%;height:220px}
  .photo--darts{background:linear-gradient(135deg,#2a2a2a 0%,#6b6b6b 40%,#d8c05a 70%,#3a3a3a 100%)}
  .photo--figures{background:linear-gradient(135deg,#f1f2f4 0%,#d9dde2 55%,#a8adb3 100%)}
  .photo--lens{background:linear-gradient(135deg,#e9edf2 0%,#c9d3dd 45%,#8fb3b4 70%,#e3e7ec 100%)}
  .service__title{margin-top:26px;font-size:18px;font-weight:700;line-height:24px;color:var(--ink);padding:0 30px}
  .service__body{margin-top:14px;font-size:15.5px;line-height:19.7px;color:var(--body);padding:0 30px}

  /* two columns */
  .column{position:absolute;top:357px;width:387px;font-size:19.5px;line-height:27.3px;color:var(--body)}
  .divider{position:absolute;width:2px;background:var(--rule)}

  /* values */
  .values__backdrop{position:absolute;inset:0;background:linear-gradient(160deg,#eef0f4 0%,#f6f6f8 45%,#e6eaf0 100%)}
  .values__panel{position:absolute;left:75px;top:331px;width:898px;height:402px;background:var(--white);box-shadow:0 2px 10px rgba(0,0,0,.08)}
  .values__text{position:absolute;left:74px;top:56px;width:306px;font-size:19.5px;line-height:27.3px}
  .values__bullets{position:absolute;left:448px;top:115px;font-size:20px;line-height:32.8px;color:var(--body)}
</style>
</head>
<body>

<!-- Cover -->
<section class="slide slide--cover">
  <svg class="cover__art" viewBox="0 0 626 470" preserveAspectRatio="none" aria-hidden="true">
    <polygon points="147,122 370,0 392,0 169,122" fill="var(--blue)"/>
    <polygon points="147,380 169,380 317,470 293,470" fill="var(--blue)"/>
    <polygon points="385,0 626,0 626,470 317,470 215,390 215,123" fill="var(--charcoal)"/>
  </svg>
  <div class="brand" style="left:40px;top:38px;width:190px">
    <div class="brand__mark"></div>
    <div class="brand__name">BRANNOW<br>ADVISORY</div>
  </div>
  <div class="abs cover__photo" role="img" aria-label="Photo of a magnifying glass and pen over a printed financial report"></div>
  <div class="abs cover__rule"></div>
  <h1 class="abs cover__title">WHY CHOOSE BRANNOW?</h1>
  <p class="abs cover__lead">Brannow Advisory was founded on the principles of innovation and teamwork. We innovate the products we implement through a combination of functional experience and technical expertise. When we find limitations in the products that we implement, we see this as an opportunity and a challenge to extend those products until we meet the needs of our clients.</p>
  <ul class="abs bullets cover__bullets">
    <li>Lorem Ipsum is simply dummy text</li>
    <li>Contrary to popular belief, Lorem Ipsum is not simply</li>
    <li>There are many variations of passage</li>
    <li>It is a long established fact that</li>
    <li>There are many variations of pass</li>
  </ul>
</section>

<!-- Three columns -->
<section class="slide slide--columns">
  <div class="brand brand--center"><div class="brand__mark"></div><div class="brand__name">BRANNOW ADVISORY</div></div>
  <h2 class="heading" style="top:205px;font-size:28px">SED UT PERSPICIATIS UNDE OMNIS ISTE NATUS</h2>
  <div class="card card--text" style="left:32px">
    <h3 class="card__title">Sed ut perspiciatis unde omnis iste natus error sit voluptatem</h3>
    <p class="card__body">On the other hand, we denounce with righteous indignation and dislike men who are so beguiled and demoralized by the charms of pleasure of the moment, so blinded by desire, that they cannot foresee the pain and trouble that are bound to ensue; and equal blame belongs to those who fail in their duty through</p>
  </div>
  <div class="card card--text" style="left:373px">
    <h3 class="card__title">Sed ut perspiciatis unde omnis iste natus error sit voluptatem</h3>
    <p class="card__body">On the other hand, we denounce with righteous indignation and dislike men who are so beguiled and demoralized by the charms of pleasure of the moment, so blinded by desire, that they cannot foresee the pain and trouble that are bound to ensue; and equal blame belongs to those who fail in their duty through</p>
  </div>
  <div class="card card--text" style="left:710px">
    <h3 class="card__title">Sed ut perspiciatis unde omnis iste natus error sit voluptatem</h3>
    <p class="card__body">On the other hand, we denounce with righteous indignation and dislike men who are so beguiled and demoralized by the charms of pleasure of the moment, so blinded by desire, that they cannot foresee the pain and trouble that are bound to ensue; and equal blame belongs to those who fail in their duty through</p>
  </div>
</section>

<!-- Services -->
<section class="slide slide--services">
  <div class="brand brand--center" style="top:36px"><div class="brand__mark"></div><div class="brand__name">BRANNOW ADVISORY</div></div>
  <h2 class="heading" style="top:200px;font-size:30px">SERVICES</h2>
  <p class="subheading" style="top:245px;font-size:20px">Brannow Advisory offers services across the entire stack of on-premises and cloud products from Veltrix.</p>
  <div class="card card--service" style="left:38px">
    <div class="service__photo photo--darts" role="img" aria-label="Photo of darts striking the centre of a dartboard"></div>
    <h3 class="service__title">BUDGETING AND FORECASTING</h3>
    <p class="service__body">Brannow specializes in both cloud and on-premise EPM solutions provided by Veltrix. For clients ready to migrate to the cloud or implement from scratch,</p>
  </div>
  <div class="card card--service" style="left:373px">
    <div class="service__photo photo--figures" role="img" aria-label="Photo of a pen resting on printed columns of figures beside a calculator"></div>
    <h3 class="service__title">CLOSE AND CONSOLIDATION</h3>
    <p class="service__body">Brannow specializes in both cloud and on-premise EPM solutions provided by Veltrix. For clients ready to migrate to the cloud or implement from scratch,</p>
  </div>
  <div class="card card--service" style="left:711px">
    <div class="service__photo photo--lens" role="img" aria-label="Photo of a magnifying glass over a printed report with bar charts"></div>
    <h3 class="service__title">REPORTING AND ANALYSIS</h3>
    <p class="service__body">Traditionally, Corvane Planning and the Veltrix Unified Planning Suite were products closely associated with Finance and Accounting departments.</p>
  </div>
</section>

<!-- Two columns -->
<section class="slide slide--twocol">
  <div class="brand brand--center" style="top:36px"><div class="brand__mark"></div><div class="brand__name">BRANNOW ADVISORY</div></div>
  <h2 class="heading" style="top:208px;font-size:32px">LOREM IPSUM IS SIMPLY DUMMY TEXT OF THE PRINTING</h2>
  <p class="subheading" style="top:257px;font-size:22px">Lorem Ipsum is simply dummy text of the printing and typesetting industry.</p>
  <p class="column" style="left:77px">There are many variations of passages of Lorem Ipsum avai lable, but the majority have suffe red alteration in some form, by injected humour, or randomised words which don't look even slig htly believable. If you are going to use a passage of Lorem Ipsum, you need to be sure there isn't anything embarrassing hidden in the middle of text On the other hand, we denounce with righteous indignation and dislike men who are so beguiled and demoralized by the charms of pleasure of the moment, so blinded by desire.</p>
  <div class="divider" style="left:523px;top:338px;height:377px"></div>
  <p class="column" style="left:594px">There are many variations of passages of Lorem Ipsum avai lable, but the majority have suffe red alteration in some form, by injected humour, or randomised words which don't look even slig htly believable. If you are going to use a passage of Lorem Ipsum, you need to be sure there isn't anything embarrassing hidden in the middle of text On the other hand, we denounce with righteous indignation and dislike men who are so beguiled and demoralized by the charms of pleasure of the moment, so blinded by desire.</p>
</section>

<!-- Core values -->
<section class="slide slide--values">
  <div class="values__backdrop" role="img" aria-label="Faint background photo of hands reviewing printed charts on a desk"></div>
  <div class="brand brand--center" style="top:36px"><div class="brand__mark"></div><div class="brand__name">BRANNOW ADVISORY</div></div>
  <h2 class="heading" style="top:206px;font-size:31px">OUR CORE VALUES PROVIDE OUR FOUNDATION</h2>
  <p class="subheading" style="top:253px;font-size:22px">Lorem Ipsum is simply dummy text of the printing and typesetting industry.</p>
  <div class="values__panel">
    <p class="values__text">There are many variations of passages of Lorem Ipsum avai lable, but the majority have suffe red alteration in some form, by injected humour, or randomised words which don't look even slig htly believable. If you are going to use a passage of Lorem Ipsum, you need to be sure there isn't anything embarrassing hidden in the middle of text</p>
    <div class="divider" style="left:447px;top:25px;height:352px"></div>
    <ul class="bullets values__bullets" style="left:428px">
      <li>Lorem Ipsum is simply dummy text</li>
      <li>Contrary to popular belief, Lorem Ipsum</li>
      <li>There are many variations of passage</li>
      <li>It is a long established fact that</li>
      <li>There are many variations of pass</li>
    </ul>
  </div>
</section>

</body>
</html>
```